we do all sorts of cleaning however bookings are limited!
why not chose the right cleaners for you!
pressure cleaning, window cleaning, office, end of lease clean, accommodation, industrial and commercial cleaning and house cleaning

Logo Text

Bright Nest Cleaning Service

```html
<!DOCTYPE html>
<html lang="en">
<head>
<meta charset="utf-8">
<title>Bright Nest Cleaning Service – Business Card</title>
<link rel="stylesheet" href="https://fonts.googleapis.com/css2?family=Poppins:wght@400;600;700&display=swap">
<style>
  :root {
    --backdrop: #666666;
    --card: #2c2c2c;
    --card-back: #292929;
    --brand-blue: #1aa3e8;
    --brand-green: #7dc242;
    --text-light: #f2f2f2;
    --divider: #6a6a6a;
    --emboss: #8c8c8c;
  }
  * { margin: 0; padding: 0; box-sizing: border-box; }
  html, body {
    width: 1200px; height: 1200px; overflow: hidden;
    background: var(--backdrop);
    font-family: "Poppins", Arial, sans-serif;
  }
  .card {
    position: absolute;
    width: 688px; height: 393px;
    border-radius: 30px;
    background: var(--card);
  }
  .card--front { left: 266px; top: 158px; }
  .card--back { left: 261px; top: 652px; background: var(--card-back); }

  .brand-mark {
    position: absolute;
    display: flex; align-items: center; gap: 10px;
  }
  .card--front .brand-mark { left: 78px; top: 160px; }
  .brand-dot {
    width: 14px; height: 14px; border-radius: 50%;
    background: var(--brand-green); flex: none;
  }
  .brand-name {
    color: var(--brand-blue);
    font-weight: 600;
    font-size: 27px;
    line-height: 1.15;
  }
  .brand-name small { font-size: inherit; display: block; }

  .divider {
    position: absolute; left: 363px; top: 81px;
    width: 2px; height: 236px;
    background: var(--divider);
  }
  .contact { position: absolute; left: 387px; top: 90px; color: var(--text-light); }
  .contact__name {
    color: var(--brand-blue); font-weight: 700; font-size: 27px;
    line-height: 1.1; letter-spacing: 0.3px;
  }
  .contact__role { font-size: 16px; line-height: 1.4; }
  .contact__address { margin-top: 16px; font-size: 17px; line-height: 21px; }
  .contact__list { list-style: none; margin-top: 12px; font-size: 17px; }
  .contact__list li { display: flex; align-items: center; height: 21px; }
  .contact__list svg { width: 14px; height: 14px; margin-right: 11px; fill: var(--brand-green); flex: none; }

  .card--back .brand-mark {
    left: 0; right: 0; top: 0; bottom: 0;
    justify-content: center;
  }
  .card--back .brand-name {
    color: var(--emboss);
    font-size: 46px;
    text-align: center;
    line-height: 1.15;
  }
</style>
</head>
<body>
  <section class="card card--front">
    <div class="brand-mark">
      <span class="brand-dot"></span>
      <span class="brand-name">Bright Nest<small>Cleaning Service</small></span>
    </div>
    <div class="divider"></div>
    <div class="contact">
      <h1 class="contact__name">DANIEL HARPER</h1>
      <p class="contact__role">President</p>
      <p class="contact__address">4210 Willow Crest Road<br>Halden, Canada 52819</p>
      <ul class="contact__list">
        <li><svg viewBox="0 0 24 24"><path d="M6.6 10.8a15 15 0 0 0 6.6 6.6l2.2-2.2c.3-.3.7-.4 1-.2 1.1.4 2.3.6 3.6.6.6 0 1 .4 1 1V20c0 .6-.4 1-1 1A17 17 0 0 1 3 4c0-.6.4-1 1-1h3.5c.6 0 1 .4 1 1 0 1.3.2 2.5.6 3.6.1.3 0 .7-.2 1z"/></svg>555-214-7890</li>
        <li><svg viewBox="0 0 24 24"><path d="M7 1h10a2 2 0 0 1 2 2v18a2 2 0 0 1-2 2H7a2 2 0 0 1-2-2V3a2 2 0 0 1 2-2zm0 3v15h10V4z"/></svg>555-386-1042</li>
        <li><svg viewBox="0 0 24 24"><path d="M2 5h20v14H2zm2 2v.5l8 5 8-5V7zm0 2.8V17h16V9.8l-8 5z"/></svg>hello@brightnest.com</li>
        <li><svg viewBox="0 0 24 24"><circle cx="12" cy="12" r="10"/></svg>www.brightnest.com</li>
      </ul>
    </div>
  </section>

  <section class="card card--back">
    <div class="brand-mark">
      <span class="brand-name">Bright Nest<small>Cleaning Service</small></span>
    </div>
  </section>
</body>
</html>
```